7Brink Plumbing flyer

I want to incorporate our logo design into a new flyer promoting the business and advertising products that we install.
We install hot water systems, Air-conditioning systems and central heating systems. Along with other aspects of plumbing such as gasfitting, roofing, sanitary and drainage
I would like the background to be the same as our business cards with the water effect and colours.

Requirements
Must have
• Logo
24/7 Emergency call out
Aspects of plumbing we do
- Hot water systems
- Central Heating
- Solar hot water systems/ heat pump systems
- Gasfitting
- Drainage
- Roofing
- Air-Conditioning
Nice to have
• Pictures of hot water systems and air-conditioning system
$30 off voucher when producing this flyer (limit 1 per house hold)

```html
<!DOCTYPE html>
<html lang="en">
<head>
<meta charset="utf-8">
<title>7Brink Plumbing Flyer</title>
<link rel="stylesheet" href="https://fonts.googleapis.com/css2?family=Poppins:wght@300;500;600&family=Oswald:wght@600;700&family=Bebas+Neue&display=swap">
<style>
  :root {
    --navy: #0c3f86;
    --navy-deep: #082c63;
    --sky: #1a9be0;
    --charcoal: #1d2127;
    --charcoal-soft: #343a42;
    --orange: #e8561c;
    --white: #ffffff;
    --ink: #1f1f1f;
  }
  * { box-sizing: border-box; margin: 0; padding: 0; }
  html, body { width: 915px; height: 1200px; overflow: hidden; background: var(--white); }
  .flyer { position: relative; width: 915px; height: 1200px; overflow: hidden; font-family: "Poppins", sans-serif; }
  .backdrop { position: absolute; inset: 0; }
  .photo-plumber {
    position: absolute; left: 380px; top: 0; width: 535px; height: 455px;
    background: linear-gradient(90deg, rgba(60,66,74,0) 0%, #aeb7bf 30%, #e7ecef 60%, #d9e2e6 100%);
  }
  .photo-heater {
    position: absolute; left: 107px; top: 238px; width: 246px; height: 273px;
    background: radial-gradient(ellipse at 40% 45%, #f1efe6 0%, #d9d6cb 55%, rgba(217,214,203,0) 75%);
  }
  .photo-aircon {
    position: absolute; left: 50px; top: 753px; width: 326px; height: 252px;
    background: radial-gradient(ellipse at 50% 50%, #f4f6f8 0%, #dde3e8 50%, rgba(221,227,232,0) 75%);
  }
  .brand { position: absolute; left: 58px; top: 40px; display: flex; align-items: center; gap: 20px; }
  .brand-dot { width: 126px; height: 126px; border-radius: 50%; background: var(--sky); flex: none; }
  .brand-name { color: var(--sky); font-weight: 600; text-transform: uppercase; line-height: 1; }
  .brand-name span { display: block; }
  .brand-line-1 { font-size: 46px; }
  .brand-line-2 { font-size: 40px; margin-top: 2px; }
  .brand-line-3 { font-size: 16px; margin-top: 6px; letter-spacing: 0.6px; }
  .intro {
    position: absolute; left: 54px; top: 553px; white-space: nowrap;
    color: var(--white); font-size: 19px; font-weight: 300; line-height: 26.5px;
  }
  .intro strong { font-weight: 600; }
  .services-panel { position: absolute; left: 495px; top: 490px; width: 382px; height: 512px; background: var(--sky); }
  .services-title {
    position: absolute; left: 461px; top: 567px; width: 332px; height: 68px;
    background: var(--navy); color: var(--white);
    font-size: 27px; font-weight: 600; line-height: 29px; padding: 4px 0 0 52px;
  }
  .services-title::before {
    content: ""; position: absolute; left: 0; top: 68px;
    border-top: 32px solid var(--navy-deep); border-left: 34px solid transparent;
  }
  .services-list { position: absolute; left: 519px; top: 653px; list-style: none; color: var(--white); }
  .services-list li { position: relative; padding-left: 37px; font-size: 23px; font-weight: 500; line-height: 31px; margin-bottom: 8px; }
  .services-list li svg { position: absolute; left: 0; top: 4px; }
  .emergency-badge { position: absolute; left: 562px; top: 340px; }
  .contact { position: absolute; left: 30px; top: 1040px; width: 380px; text-align: center; }
  .contact-cta { font-family: "Bebas Neue", sans-serif; font-size: 48px; color: var(--ink); line-height: 1; letter-spacing: 0.5px; }
  .contact-phone { font-family: "Bebas Neue", sans-serif; font-size: 72px; color: var(--navy); line-height: 1; margin-top: 4px; letter-spacing: 0.5px; }
  .contact-email { font-size: 22.5px; font-weight: 500; color: var(--sky); margin-top: 2px; }
  .voucher { position: absolute; left: 481px; top: 1045px; width: 396px; height: 132px; }
  .voucher svg { position: absolute; inset: 0; }
  .voucher-amount { position: absolute; left: 20px; top: 26px; font-family: "Bebas Neue", sans-serif; font-size: 100px; line-height: 0.8; color: var(--white); }
  .voucher-off { position: absolute; left: 141px; top: 61px; transform: rotate(-90deg); font-family: "Bebas Neue", sans-serif; font-size: 32px; line-height: 1; color: var(--white); }
  .voucher-label { position: absolute; left: 206px; top: 32px; width: 176px; text-align: center; }
  .voucher-label b { display: block; font-family: "Bebas Neue", sans-serif; font-weight: 400; font-size: 50px; line-height: 0.9; color: var(--sky); letter-spacing: 0.5px; }
  .voucher-label small { display: block; font-family: "Oswald", sans-serif; font-weight: 600; font-size: 11.5px; color: var(--white); margin-top: 10px; }
</style>
</head>
<body>
<main class="flyer">
  <svg class="backdrop" width="915" height="1200" viewBox="0 0 915 1200" aria-hidden="true">
    <defs>
      <linearGradient id="top-dark" x1="0" y1="0" x2="1" y2="1">
        <stop offset="0" stop-color="var(--charcoal)"/>
        <stop offset="1" stop-color="var(--charcoal-soft)"/>
      </linearGradient>
      <linearGradient id="deep-water" x1="0" y1="0" x2="0" y2="1">
        <stop offset="0" stop-color="#0a3a7c"/>
        <stop offset="1" stop-color="#0d4a99"/>
      </linearGradient>
    </defs>
    <rect x="0" y="0" width="915" height="480" fill="url(#top-dark)"/>
    <path d="M0 470 Q180 440 380 470 Q560 495 700 445 Q820 410 915 455 L915 1010 L0 1010 Z" fill="url(#deep-water)"/>
    <path d="M40 480 Q200 415 390 455 Q560 490 690 440" fill="none" stroke="var(--sky)" stroke-width="11"/>
    <path d="M760 430 Q840 420 905 445" fill="none" stroke="var(--sky)" stroke-width="4"/>
    <path d="M0 1013 Q220 960 470 990 Q720 1020 915 978 L915 1200 L0 1200 Z" fill="var(--white)"/>
    <path d="M90 1022 Q300 985 470 1008 Q700 1035 830 1012" fill="none" stroke="var(--sky)" stroke-width="8"/>
  </svg>

  <div class="photo-plumber" role="img" aria-label="Photo of a smiling plumber in navy work uniform holding a tap and a pipe wrench in a kitchen, with a tool bag on the bench"></div>
  <div class="photo-heater" role="img" aria-label="Product photo of a heat pump hot water tank with its outdoor unit"></div>
  <div class="photo-aircon" role="img" aria-label="Product photos of split system air-conditioners: ceiling cassette, wall unit, floor unit and outdoor unit"></div>

  <div class="brand">
    <div class="brand-dot"></div>
    <div class="brand-name">
      <span class="brand-line-1">7Brink</span>
      <span class="brand-line-2">Plumbing</span>
      <span class="brand-line-3">&amp; Air-Conditioning</span>
    </div>
  </div>

  <p class="intro">We install hot water systems,<br><strong>Air-conditioning systems and</strong><br><strong>central heating systems.</strong> Along with<br>other aspects of plumbing such as<br><strong>gasfitting, roofing, sanitary and</strong><br><strong>drainage</strong></p>

  <div class="services-panel"></div>
  <h2 class="services-title">Aspects of<br>Plumbing we do</h2>
  <ul class="services-list">
    <li><svg width="18" height="22" viewBox="0 0 18 22" aria-hidden="true"><path d="M9 1 C13 7 17 11 17 15 A8 7 0 0 1 1 15 C1 11 5 7 9 1Z" fill="var(--white)"/></svg>Hot water systems</li>
    <li><svg width="18" height="22" viewBox="0 0 18 22" aria-hidden="true"><path d="M9 1 C13 7 17 11 17 15 A8 7 0 0 1 1 15 C1 11 5 7 9 1Z" fill="var(--white)"/></svg>Central Heating</li>
    <li><svg width="18" height="22" viewBox="0 0 18 22" aria-hidden="true"><path d="M9 1 C13 7 17 11 17 15 A8 7 0 0 1 1 15 C1 11 5 7 9 1Z" fill="var(--white)"/></svg>Solar hot water systems/<br>heat pump systems</li>
    <li><svg width="18" height="22" viewBox="0 0 18 22" aria-hidden="true"><path d="M9 1 C13 7 17 11 17 15 A8 7 0 0 1 1 15 C1 11 5 7 9 1Z" fill="var(--white)"/></svg>Gasfitting</li>
    <li><svg width="18" height="22" viewBox="0 0 18 22" aria-hidden="true"><path d="M9 1 C13 7 17 11 17 15 A8 7 0 0 1 1 15 C1 11 5 7 9 1Z" fill="var(--white)"/></svg>Drainage</li>
    <li><svg width="18" height="22" viewBox="0 0 18 22" aria-hidden="true"><path d="M9 1 C13 7 17 11 17 15 A8 7 0 0 1 1 15 C1 11 5 7 9 1Z" fill="var(--white)"/></svg>Roofing</li>
    <li><svg width="18" height="22" viewBox="0 0 18 22" aria-hidden="true"><path d="M9 1 C13 7 17 11 17 15 A8 7 0 0 1 1 15 C1 11 5 7 9 1Z" fill="var(--white)"/></svg>Air-Conditioning</li>
  </ul>

  <svg class="emergency-badge" width="196" height="196" viewBox="0 0 196 196" role="img" aria-label="Emergency 24/7 service">
    <defs>
      <path id="arc-top" d="M40 113.5 A60 60 0 0 1 140.4 55.6"/>
      <path id="arc-bottom" d="M69.3 159.6 A68 68 0 0 0 165 109.8"/>
    </defs>
    <circle cx="98" cy="98" r="96" fill="var(--white)"/>
    <circle cx="98" cy="98" r="90" fill="var(--navy)"/>
    <circle cx="98" cy="98" r="80" fill="var(--white)"/>
    <circle cx="98" cy="98" r="75" fill="var(--orange)"/>
    <path d="M146 59 A62 62 0 0 1 159 96" fill="none" stroke="var(--white)" stroke-width="2.5"/>
    <path d="M146 59 l-1 -9 l9 4 z" fill="var(--white)"/>
    <path d="M65 151 A62 62 0 0 1 39 118" fill="none" stroke="var(--white)" stroke-width="2.5"/>
    <path d="M65 151 l-1 9 l9 -5 z" fill="var(--white)"/>
    <text font-family="Oswald, sans-serif" font-weight="700" font-size="14" fill="var(--white)" letter-spacing="1.5"><textPath href="#arc-top" startOffset="50%" text-anchor="middle">EMERGENCY</textPath></text>
    <text font-family="Oswald, sans-serif" font-weight="700" font-size="14" fill="var(--white)" letter-spacing="1.5"><textPath href="#arc-bottom" startOffset="50%" text-anchor="middle">SERVICE</textPath></text>
    <text x="98" y="118" text-anchor="middle" font-family="Oswald, sans-serif" font-weight="700" font-size="52" fill="var(--white)">24/7</text>
  </svg>

  <div class="contact">
    <div class="contact-cta">CALL TODAY</div>
    <div class="contact-phone">0400 555 123</div>
    <div class="contact-email">sam@7brinkplumbing.com</div>
  </div>

  <div class="voucher">
    <svg width="396" height="132" viewBox="0 0 396 132" aria-hidden="true">
      <rect x="0" y="0" width="396" height="132" fill="var(--navy)"/>
      <path d="M0 0 H180 Q200 66 186 132 H0 Z" fill="var(--sky)"/>
      <path d="M180 0 Q200 66 186 132" fill="none" stroke="var(--white)" stroke-width="3"/>
      <rect x="5" y="5" width="386" height="122" fill="none" stroke="var(--white)" stroke-width="1.5" stroke-dasharray="6 5"/>
    </svg>
    <div class="voucher-amount">$30</div>
    <div class="voucher-off">OFF</div>
    <div class="voucher-label"><b>VOUCHER</b><small>WHEN PRODUCING THIS FLYER</small></div>
  </div>
</main>
</body>
</html>
```